Web Concept Design - modernize website

Looking to modernize our current website. http :// hvmcoldbrook . com

Color Scheme: Use uploaded palette. (Black, Silver, Dark Purple, Greyish Blue)

The website needs to have a patient-friendly, community-friendly feel to it. While still being a professional medical website. We don't want it to have a cold, clinical feel.

Information on home page needs to be split into their own separate pages with designs for each.

Home Page:
Harborview Walk-In & Family Care is a family practice and urgent care clinic dedicated to providing high quality, compassionate health care, to patients of all ages.
Hours of operation:
Monday-Friday 9am-6:30pm
Saturday: CLOSED
Sunday: CLOSED
Primary Care visits will be by appointment only.
We will accept our last new patient at 6:00p and our last established patient at 6:30p.
We will no longer be doing DOT Physicals.

At bottom of home page:

Harborview Walk-In & Family Care understands that information about your health is private and we know how important it is to keep your medical information protected. We follow all HIPAA guidelines to protect the privacy of your medical records. The privacy act below explains our privacy practices and how we may use and disclose your medical information. If you would like for Harborview Walk-In & Family Care to release any or all of your medical information to others, you can make the request by signing a release and bring it with you at your next visit. If you would like to contact someone about the privacy and/or use of your medical information, you may contact us at 205-381-7260.

Click here for HIPAA document.

Click here for Medical Release form.

---------------

Services Page:
We provide family and urgent care for patients of all ages.

-Annual physicals
-Pre-employment drug screening
-Women's care including pap smears
-Screening and treatment for diabetes, hypertension and cholesterol
-All minor trauma such as abscesses, lacerations, burns and fractures
-Minor skin complaints
-Onsite LAB/XRAY/EKG
-Weight loss
-Adult and Pediatric Vaccinations
-Osteopathic manual medicine
-Medical pain management

-----

Payment & Insurance Page:
We now have online bill pay for patient balances. Please visit https://secure.paytrellixmed.example/hvmc382pay to pay your bill today!

We currently accept all forms of insurance with the exception of Medicaid. Please bring a copy of your insurance card and photo ID upon visit. We are also a Servimed prime provider. We do accept self-pay for patients who do not have insurance.

----

Meet Our Providers Page:

Dr. Daniel (Dan) Whitcomb, DO
Family Practice Physician

Professional Experience
April 4, 2010 to Present Harborview Walk-In & Family Care Owner
12 years of Emergency Medicine experience
6/1994 - 7/1997 KLT Birmingham, AL
Family Medicine Residency
10/1997 to Present Board Certified in Family Medicine
Recertified 2004
Education
9/1990 to 5/1994 Eastbrook College of Osteopathic Medicine
Old Westbury, New York
Degree: Doctor of Osteopathic Medicine
9/1985 to 5/1989 Caldwell-Ridgemont College
Birmingham, Alabama
Degree: Bachelor of Science
Membership
National Guild of Family Practitioners
Physicians Council of the State of Alabama

----

Navigation Bar should have links for all the above pages + NEW PATIENTS + Access Your Medical Records (feel free to be creative with how you design this). We don't want the navigation bar to be too crowded.

Target Market(s)

Medical Patients

Number of Pages Required

5+ page

Colors

Designer to choose colors to be used in the design.

Requirements
Must have
• Designs for all pages
• Keep it professional
Nice to have
• Be creative!
Should not have
• No cold clinical, medical websites

```html
<!DOCTYPE html>
<html lang="en">
<head>
<meta charset="utf-8">
<title>Harborview Walk-In &amp; Family Care</title>
<link rel="stylesheet" href="https://fonts.googleapis.com/css2?family=Arimo:wght@400;700&display=swap">
<style>
  :root {
    --navy-deep: #060d1c;
    --navy: #0c1a33;
    --hero-glow: #2a4f7e;
    --white: #ffffff;
    --link-blue: #1a5fc4;
    --bar-grey: #f1f2f5;
    --bar-line: #dfe1e6;
    --text-muted: #6b7487;
    --heading-navy: #1f2a52;
    --label-blue: #8d9ab8;
    --body-grey: #6a7080;
    --icon-a: #4a5f9a;
    --icon-b: #4aa3df;
    --icon-c: #c9473b;
    --photo-a: #d9d4cc;
    --photo-b: #8a7866;
  }
  * { box-sizing: border-box; margin: 0; padding: 0; }
  html, body { width: 1200px; height: 676px; overflow: hidden; }
  body {
    font-family: "Arimo", Arial, sans-serif;
    background: var(--white);
    position: relative;
  }
  .site-header {
    position: absolute; left: 0; top: 0; width: 1200px; height: 70px;
    background: var(--navy-deep);
    border-bottom: 1px solid rgba(255,255,255,0.18);
    display: flex; align-items: center;
    z-index: 2;
  }
  .brand {
    position: absolute; left: 48px; top: 12px;
    color: var(--white); font-size: 17px; line-height: 22px; font-weight: 400;
    width: 190px;
  }
  .main-nav {
    position: absolute; left: 425px; top: 28px;
    display: flex; gap: 32px;
  }
  .main-nav a {
    color: var(--white); text-decoration: none;
    font-size: 13px; font-weight: 700; letter-spacing: 0.2px;
  }
  .header-actions {
    position: absolute; right: 40px; top: 22px; display: flex; gap: 6px;
  }
  .btn-outline, .btn-solid {
    font-size: 12px; padding: 6px 10px; border-radius: 14px; text-decoration: none;
  }
  .btn-outline { color: var(--white); border: 1.5px solid var(--white); }
  .btn-solid { color: var(--navy); background: var(--white); border: 1.5px solid var(--white); }

  .hero {
    position: absolute; left: 0; top: 0; width: 1200px; height: 488px;
    background:
      radial-gradient(ellipse 55% 35% at 72% 78%, rgba(90,140,200,0.55), transparent 70%),
      radial-gradient(ellipse 70% 30% at 50% 92%, rgba(60,110,170,0.45), transparent 75%),
      linear-gradient(180deg, var(--navy-deep) 0%, var(--navy) 45%, var(--hero-glow) 100%);
    text-align: center; color: var(--white);
  }
  .hero-title { position: absolute; top: 205px; width: 100%; font-size: 29px; font-weight: 400; }
  .hero-lines { position: absolute; top: 260px; width: 100%; font-size: 17px; line-height: 30px; }
  .hero-cta {
    position: absolute; top: 338px; left: 50%; transform: translateX(-50%);
    background: var(--white); color: var(--link-blue); text-decoration: none;
    font-size: 14px; padding: 9px 22px; border-radius: 18px;
  }

  .sub-bar {
    position: absolute; left: 0; top: 488px; width: 1200px; height: 32px;
    background: var(--bar-grey); border-bottom: 1px solid var(--bar-line);
    display: flex; align-items: center; padding-left: 48px; font-size: 12px;
  }
  .sub-bar .label { color: var(--text-muted); font-weight: 700; margin-right: 12px; }
  .sub-bar a { color: var(--text-muted); text-decoration: none; margin-right: 22px; }
  .social { position: absolute; right: 52px; top: 9px; display: flex; gap: 20px; align-items: center; }
  .social span { width: 13px; height: 13px; border-radius: 2px; display: block; }
  .social .s1 { background: var(--icon-a); }
  .social .s2 { background: var(--icon-b); }
  .social .s3 { background: var(--icon-c); }

  .about { position: absolute; left: 58px; top: 555px; width: 560px; }
  .about-label { color: var(--label-blue); font-size: 14px; }
  .about-title { color: var(--heading-navy); font-size: 26px; font-weight: 400; margin-top: 6px; }
  .about-text { color: var(--body-grey); font-size: 11.5px; line-height: 20px; margin-top: 18px; }

  .about-photo {
    position: absolute; left: 735px; top: 590px; width: 395px; height: 86px;
    background: linear-gradient(100deg, var(--photo-a) 0%, var(--photo-b) 55%, var(--photo-a) 100%);
  }
</style>
</head>
<body>
  <section class="hero">
    <h1 class="hero-title">Primary Care visits will be by appointment only</h1>
    <p class="hero-lines">We will accept our last new patient at 6:00p<br>and our last established patient at 6:30p</p>
    <a class="hero-cta" href="#">Schedule a Appointment</a>
  </section>

  <header class="site-header">
    <div class="brand">Harborview Walk-In &amp;<br>Family Care</div>
    <nav class="main-nav">
      <a href="#">SERVICES</a>
      <a href="#">OUR PROVIDERS</a>
      <a href="#">CONTACT US</a>
    </nav>
    <div class="header-actions">
      <a class="btn-outline" href="#">Log In</a>
      <a class="btn-solid" href="#">Make a Appointment</a>
    </div>
  </header>

  <nav class="sub-bar">
    <span class="label">Learn More:</span>
    <a href="#">Our Clinic</a>
    <a href="#">Blog</a>
    <a href="#">Careers</a>
    <a href="#">Help &amp; Contact</a>
    <div class="social">
      <span class="s1"></span><span class="s2"></span><span class="s3"></span>
      <svg width="12" height="12" viewBox="0 0 12 12" aria-label="Search"><circle cx="5" cy="5" r="3.6" fill="none" stroke="#6b7487" stroke-width="1.5"/><line x1="7.6" y1="7.6" x2="11" y2="11" stroke="#6b7487" stroke-width="1.6"/></svg>
    </div>
  </nav>

  <section class="about">
    <p class="about-label">About Us</p>
    <h2 class="about-title">Who we are ?</h2>
    <p class="about-text">Harborview Walk-In &amp; Family Care is a family practice and urgent care clinic dedicated to providing<br>high quality, compassionate health care, to patients of all ages.</p>
  </section>

  <div class="about-photo" role="img" aria-label="Photo of the clinic team in a meeting"></div>
</body>
</html>
```